Business Cards Needed for Innovative Healthcare Marketing Company

We are a marketing company focused on healthcare. Our company is all about rebranding yourself renewing your image and generating results. The phoenix stands for "reborn" or "rising" which we provide new brands for our clients we take their old brands and renew it with creativity and innovation. I am looking for a business card with color dimension. I have attached an example of a card I think has the look and feel of what I am trying to accomplish. I like that the card example has black and grey font colors, I like the font placement and the small logo, I really like the use of the colors on the right those are the colors of my logo. My logo is phoenix so maybe incorporating flames similar to that design. I would like the back a solid color maybe red with an opaque version of the logo and website. As a marketing company I am always open to creative liberty!

Target Market(s)

Doctors and business professionals.

Industry/Entity Type

Marketing

Contact Information for Business Card

Vornaly Health Care Marketing
Marnie Okonski- CEO
#(502)638-2947
email-marnie@vornaly.com
website- vornaly.com

Font styles to use
Sans Serif

Colors
ec1f27
f37122
ffc214
fbed22
fbf289
f04a50

Requirements
Must have
• The logo and required information
Nice to have
• icons by the information
Should not have
• child like font

```html
<!DOCTYPE html>
<html lang="en">
<head>
<meta charset="utf-8">
<title>Vornaly Health Care Marketing – Business Cards</title>
<link rel="stylesheet" href="https://fonts.googleapis.com/css2?family=Montserrat:wght@400;500;700&display=swap">
<style>
  :root {
    --bg: #2b2b2d;
    --brand-red: #a3252a;
    --brand-orange: #f39a1e;
    --name-orange: #f2a019;
    --paper: #ffffff;
    --ink: #2a2a2a;
    --muted-red: #b4474b;
  }
  * { margin: 0; padding: 0; box-sizing: border-box; }
  html, body { width: 1200px; height: 900px; overflow: hidden; }
  body {
    background: var(--bg);
    font-family: "Montserrat", Arial, sans-serif;
    position: relative;
  }
  .card {
    position: absolute;
    width: 700px;
    height: 400px;
    border-radius: 26px;
    overflow: hidden;
    box-shadow: 0 18px 40px rgba(0,0,0,0.45);
  }
  .card-shapes { position: absolute; inset: 0; }
  .card--back { left: 110px; top: 40px; background: var(--brand-red); }
  .card--front { left: 390px; top: 460px; background: var(--paper); }

  .brand { position: absolute; display: flex; align-items: center; gap: 16px; }
  .brand-dot { width: 62px; height: 62px; border-radius: 50%; flex: none; }
  .brand-name {
    font-weight: 400;
    line-height: 1.1;
    text-transform: uppercase;
  }
  .brand-name .word { display: block; font-size: 46px; letter-spacing: 2px; }
  .brand-name .tagline { display: block; font-size: 15px; letter-spacing: 1.5px; }

  .card--back .brand { left: 190px; top: 130px; color: var(--paper); }
  .card--back .brand-dot { background: var(--paper); }
  .back-url {
    position: absolute; left: 40px; top: 352px;
    color: var(--brand-red); font-size: 17px; font-weight: 500; letter-spacing: 0.5px;
  }

  .card--front .brand { left: 40px; top: 60px; color: var(--muted-red); }
  .card--front .brand-dot { background: var(--brand-orange); }
  .card--front .brand-name .word { font-size: 40px; }
  .card--front .brand-name .tagline { font-size: 13px; }

  .person { position: absolute; right: 48px; top: 120px; text-align: right; }
  .person-name {
    color: var(--name-orange); font-weight: 700; font-size: 22px; letter-spacing: 0.5px;
    text-transform: uppercase;
  }
  .person-role { color: var(--ink); font-size: 14px; margin-top: 2px; }

  .contact-list { position: absolute; left: 190px; top: 228px; list-style: none; }
  .contact-item {
    display: flex; align-items: center; gap: 10px;
    color: var(--ink); font-size: 17px; line-height: 26px;
  }
  .contact-icon { width: 13px; height: 13px; flex: none; }
</style>
</head>
<body>

<section class="card card--back" aria-label="Card back">
  <svg class="card-shapes" width="700" height="400" viewBox="0 0 700 400" aria-hidden="true">
    <polygon points="400,343 700,343 700,362 420,362" fill="var(--brand-orange)"/>
    <polygon points="0,330 370,330 410,362 700,362 700,400 0,400" fill="var(--paper)"/>
  </svg>
  <div class="brand">
    <span class="brand-dot"></span>
    <span class="brand-name"><span class="word">Vornaly</span><span class="tagline">Health Care Marketing</span></span>
  </div>
  <div class="back-url">www.vornaly.com</div>
</section>

<section class="card card--front" aria-label="Card front">
  <svg class="card-shapes" width="700" height="400" viewBox="0 0 700 400" aria-hidden="true">
    <line x1="170" y1="182" x2="655" y2="182" stroke="var(--brand-red)" stroke-width="2"/>
    <polygon points="0,388 500,388 530,318 560,318 530,400 0,400" fill="var(--brand-orange)"/>
    <polygon points="548,280 700,280 700,400 520,400" fill="var(--brand-red)"/>
  </svg>
  <div class="brand">
    <span class="brand-dot"></span>
    <span class="brand-name"><span class="word">Vornaly</span><span class="tagline">Health Care Marketing</span></span>
  </div>
  <div class="person">
    <div class="person-name">Marnie Okonski</div>
    <div class="person-role">CEO</div>
  </div>
  <ul class="contact-list">
    <li class="contact-item">
      <svg class="contact-icon" viewBox="0 0 24 24" aria-hidden="true"><path fill="var(--brand-orange)" d="M6.6 10.8a15.1 15.1 0 0 0 6.6 6.6l2.2-2.2c.3-.3.7-.4 1-.2 1.1.4 2.3.6 3.6.6.6 0 1 .4 1 1V20c0 .6-.4 1-1 1C10.6 21 3 13.4 3 4c0-.6.4-1 1-1h3.5c.6 0 1 .4 1 1 0 1.3.2 2.5.6 3.6.1.3 0 .7-.2 1z"/></svg>
      (502)638-2947
    </li>
    <li class="contact-item">
      <svg class="contact-icon" viewBox="0 0 24 24" aria-hidden="true"><rect x="2" y="5" width="20" height="14" rx="1.5" fill="none" stroke="var(--brand-orange)" stroke-width="2.4"/><path d="M2.5 6l9.5 7 9.5-7" fill="none" stroke="var(--brand-orange)" stroke-width="2.4"/></svg>
      marnie@vornaly.com
    </li>
    <li class="contact-item">
      <svg class="contact-icon" viewBox="0 0 24 24" aria-hidden="true"><circle cx="12" cy="12" r="10" fill="none" stroke="var(--brand-orange)" stroke-width="2.2"/><path d="M2 12h20M12 2c3 3 3 17 0 20M12 2c-3 3-3 17 0 20" fill="none" stroke="var(--brand-orange)" stroke-width="1.8"/></svg>
      www.vornaly.com
    </li>
  </ul>
</section>

</body>
</html>
```